Belvoro Website

I need a website for a startup company that provides GIS (Geographic Information Services) staffing and products for local cities. Current website is www.belvorogroup.com

```html
<!DOCTYPE html>
<html lang="en">
<head>
<meta charset="utf-8">
<title>Belvoro Group</title>
<link href="https://fonts.googleapis.com/css2?family=DM+Sans:wght@400;500;700&family=Jost:wght@500;600;700&family=Tinos:wght@700&display=swap" rel="stylesheet">
<style>
:root{
  --blue:#1a6bb0;
  --navy:#0d1a33;
  --footer:#0a1322;
  --white:#ffffff;
  --ink:#1b1b1b;
  --field:#e6e8eb;
}
*{box-sizing:border-box;margin:0;padding:0}
html,body{width:1200px;height:3674px;overflow:hidden}
body{position:relative;background:var(--white);font-family:"DM Sans",sans-serif;color:var(--ink)}
.abs{position:absolute}
.btn{position:absolute;display:flex;align-items:center;justify-content:center;background:var(--blue);color:var(--white);font-family:"Jost",sans-serif;font-weight:500;border-radius:20px}
.media{position:absolute;overflow:hidden}

/* hero */
.hero{position:absolute;left:0;top:0;width:1200px;height:601px;
  background:radial-gradient(ellipse 620px 560px at 1010px 470px,#2a4f86 0%,#14284e 45%,transparent 75%),linear-gradient(180deg,#0e1c3a,#0a1530 60%,#13244a)}
.nav{position:absolute;left:40px;top:46px;width:1126px;height:64px;border:1px solid rgba(255,255,255,.45);border-radius:32px;background:rgba(255,255,255,.08)}
.brand{position:absolute;display:flex;align-items:center;gap:14px;font-family:"Jost",sans-serif;font-weight:600;color:var(--white)}
.brand-dot{width:20px;height:20px;border-radius:50%;background:var(--blue)}
.nav .brand{left:26px;top:14px;font-size:28px}
.nav-links{position:absolute;right:14px;top:12px;display:flex;align-items:center;gap:40px;font-family:"Jost",sans-serif;font-weight:500;font-size:19px;color:var(--white)}
.nav-links .cta{background:var(--blue);padding:5px 12px;border-radius:20px}
.hero h1{position:absolute;left:64px;top:228px;font-family:"Jost",sans-serif;font-weight:700;font-size:42px;color:var(--white)}
.hero p{position:absolute;left:64px;top:314px;width:560px;font-size:18px;line-height:24.5px;color:var(--white)}

/* about */
.about-title{position:absolute;left:646px;top:696px;font-family:"Jost",sans-serif;font-weight:600;font-size:40px;color:var(--blue)}
.about-text{position:absolute;left:646px;top:767px;width:496px;font-size:13.2px;line-height:22.6px;color:var(--ink)}

/* services */
.services{position:absolute;left:0;top:1077px;width:1200px;height:909px;
  background:radial-gradient(ellipse 500px 300px at 300px 300px,#3a2a1c 0%,transparent 70%),radial-gradient(ellipse 600px 300px at 900px 250px,#2c2418 0%,transparent 70%),linear-gradient(180deg,#101a33,#1a1614 50%,#120f14)}
.section-title{position:absolute;left:0;width:1200px;text-align:center;font-family:"Jost",sans-serif;font-weight:600;font-size:40px}
.section-lead{position:absolute;left:205px;width:790px;text-align:center;font-size:13.2px;line-height:22.5px}
.tab{position:absolute;top:1266px;height:54px;display:flex;align-items:center;justify-content:center;font-family:"Jost",sans-serif;font-weight:500;font-size:22px;color:var(--white)}
.tab.active{border:1px solid rgba(255,255,255,.5);border-radius:27px;background:rgba(255,255,255,.12)}
.card{position:absolute;border-radius:14px;overflow:hidden}
.card-label{position:absolute;left:24px;bottom:22px;font-family:"Jost",sans-serif;font-weight:700;font-size:19px;color:var(--white)}
.card .shade{position:absolute;inset:0;background:linear-gradient(180deg,transparent 55%,rgba(0,0,0,.55))}
.product-card .card-label{left:0;width:100%;text-align:center}

/* cta */
.cta-band{position:absolute;left:61px;top:2554px;width:1076px;height:264px;border-radius:14px;background:linear-gradient(180deg,#1b2230,#2a2a2c 55%,#151821)}
.cta-band h2{position:absolute;left:72px;top:88px;font-family:"Jost",sans-serif;font-weight:600;font-size:38px;line-height:45px;color:var(--white)}
.btn-square{border-radius:0;font-size:19px}
.btn-outline{background:transparent;border:1.5px solid var(--white)}

/* contact */
.contact{position:absolute;left:0;top:2882px;width:1200px;height:504px;background:linear-gradient(135deg,#0f3a5c,#163f5e 50%,#1c4868)}
.contact h2{position:absolute;left:64px;top:111px;font-family:"Jost",sans-serif;font-weight:600;font-size:38px;color:var(--white)}
.contact-lead{position:absolute;left:64px;top:183px;width:310px;font-size:13px;line-height:18px;color:var(--white)}
.contact-row{position:absolute;left:64px;display:flex;align-items:center;gap:20px;font-size:12.5px;font-weight:700;line-height:17px;color:var(--white)}
.icon-circle{width:38px;height:38px;border-radius:50%;background:var(--white);display:flex;align-items:center;justify-content:center}
.form-card{position:absolute;left:594px;top:70px;width:543px;height:366px;border-radius:24px;background:var(--white)}
.form-card h3{position:absolute;left:0;top:26px;width:100%;text-align:center;font-family:"Tinos",serif;font-weight:700;font-size:32px;color:var(--blue)}
.field{position:absolute;height:29px;border-radius:15px;background:var(--field);font-size:11px;color:#8a8d91;padding:8px 16px}
.field.msg{height:87px;border-radius:14px;padding:12px 16px;font-size:13px}
.send{position:absolute;left:58px;top:286px;width:425px;height:41px;border-radius:21px;background:var(--blue);color:var(--white);font-family:"Jost",sans-serif;font-size:20px;display:flex;align-items:center;justify-content:center}

/* footer */
.footer{position:absolute;left:0;top:3386px;width:1200px;height:288px;background:var(--footer);color:var(--white)}
.footer .brand{left:68px;top:74px;font-size:29px}
.footer-text{position:absolute;left:57px;top:166px;width:300px;font-size:13px;line-height:17px}
.footer-col{position:absolute;top:50px}
.footer-col h4{font-family:"Jost",sans-serif;font-weight:600;font-size:15px;margin-bottom:12px}
.footer-col h4 span{color:var(--blue)}
.footer-col ul{list-style:none}
.footer-col li{font-size:13px;line-height:26px;padding-left:14px;position:relative}
.footer-col li::before{content:"";position:absolute;left:0;top:11px;width:5px;height:5px;border-radius:50%;background:var(--white)}
.footer-rule{position:absolute;left:0;top:243px;width:1200px;height:1px;background:rgba(255,255,255,.5)}
.footer-bottom{position:absolute;top:256px;font-size:13px}
</style>
</head>
<body>

<header class="hero" role="img" aria-label="Earth from space at night with glowing network connection lines">
  <nav class="nav">
    <div class="brand"><span class="brand-dot"></span>Belvoro Group</div>
    <div class="nav-links"><span>Home</span><span>About us</span><span>Services</span><span>Products</span><span class="cta">Contact us</span></div>
  </nav>
  <h1>We Make GIS Work For You</h1>
  <p>We are an innovative team of geospatial experts with 25 years of experience in the field of GIS. We specialize in providing results-driven GIS solutions for local government and the private sector.</p>
  <div class="btn" style="left:64px;top:421px;width:140px;height:35px;font-size:18px">Learn more</div>
</header>

<section>
  <div class="media" role="img" aria-label="Night satellite view of Europe with city lights" style="left:63px;top:671px;width:513px;height:338px;border-radius:22px;background:radial-gradient(ellipse at 55% 55%,#5a4a2a,#1b2a40 55%,#0c1626)"></div>
  <h2 class="about-title">About us</h2>
  <p class="about-text">Lorem ipsum dolor sit amet, consectetuer adipiscing elit, sed diam nonummy nibh euismod tincidunt ut laoreet dolore magna aliquam erat volutpat. Ut wisi enim ad minim veniam, quis nostrud exerci tation ullamcorper suscipit lobortis nisl ut aliquip ex ea commodo consequat. Duis autem vel eum iriure dolor in hendrerit in vulputate velit esse molestie consequat, vel illum dolore eu feugiat nulla facilisis at vero eros et accumsan et iusto odio dignissim qui blandit praesent luptatum</p>
  <div class="btn" style="left:646px;top:943px;width:139px;height:37px;font-size:18px">Learn more</div>
</section>

<section class="services" role="img" aria-label="Dark backdrop of Earth with glowing city lights"></section>
<h2 class="section-title" style="top:1130px;color:var(--white)">Services</h2>
<p class="section-lead" style="top:1195px;color:var(--white)">Lorem ipsum dolor sit amet, consectetuer adipiscing elit, sed diam nonummy nibh euismod tincidunt ut laoreet dolore magna aliquam erat volutpat. Ut wisi enim ad minim veniam, quis nostrud exerci tation ullamcorper suscipit lobortis nisl ut</p>
<div class="tab active" style="left:63px;width:348px">GIS Consulting</div>
<div class="tab" style="left:425px;width:350px">Spatial Data Solutions</div>
<div class="tab" style="left:788px;width:324px">GIS Applications</div>

<div class="card" style="left:63px;top:1381px;width:348px;height:264px"><div class="media" role="img" aria-label="Man reading a paper map outdoors" style="inset:0;background:linear-gradient(135deg,#8a7a4a,#6b7a6a 50%,#2a2a2a)"></div><div class="shade"></div><span class="card-label">GIS projects</span></div>
<div class="card" style="left:425px;top:1381px;width:350px;height:264px"><div class="media" role="img" aria-label="Team meeting around a laptop" style="inset:0;background:linear-gradient(135deg,#d8d8d8,#8a8a8a 50%,#3a3a3a)"></div><div class="shade"></div><span class="card-label">Staffing solutions</span></div>
<div class="card" style="left:788px;top:1381px;width:349px;height:264px"><div class="media" role="img" aria-label="Engineer working on a system diagram at a desk" style="inset:0;background:linear-gradient(135deg,#c8d8e8,#6a86a8 55%,#2a3a5a)"></div><div class="shade"></div><span class="card-label">System architecture design</span></div>
<div class="card" style="left:63px;top:1660px;width:348px;height:264px"><div class="media" role="img" aria-label="Hand touching a map on a tablet" style="inset:0;background:linear-gradient(135deg,#3a4a5a,#5a7a86 45%,#1a1a22)"></div><div class="shade"></div><span class="card-label">GIS analysis</span></div>
<div class="card" style="left:425px;top:1660px;width:350px;height:264px"><div class="media" role="img" aria-label="City street crowd at sunset with data lines" style="inset:0;background:linear-gradient(135deg,#5a4a3a,#d8b07a 55%,#3a2c22)"></div><div class="shade"></div><span class="card-label">Demographics</span></div>
<div class="card" style="left:788px;top:1660px;width:349px;height:264px"><div class="media" role="img" aria-label="Man with laptop in front of a world map screen" style="inset:0;background:linear-gradient(135deg,#dfe6ee,#9aa8b8 55%,#4a5666)"></div><div class="shade"></div><span class="card-label">Map products</span></div>

<h2 class="section-title" style="top:2040px;color:var(--blue)">Product</h2>
<p class="section-lead" style="top:2112px;color:var(--ink)">Lorem ipsum dolor sit amet, consectetuer adipiscing elit, sed diam nonummy nibh euismod tincidunt ut laoreet dolore magna aliquam erat volutpat. Ut wisi enim ad minim veniam, quis nostrud exerci tation ullamcorper suscipit lobortis nisl ut</p>

<div class="card product-card" style="left:63px;top:2216px;width:258px;height:264px"><div class="media" role="img" aria-label="Figure in front of glowing data screens" style="inset:0;background:linear-gradient(180deg,#1f4a5a,#2a5a66 45%,#0c1a22)"></div><div class="shade"></div><span class="card-label">TerraView</span></div>
<div class="card product-card" style="left:334px;top:2216px;width:260px;height:264px"><div class="media" role="img" aria-label="Glowing 3D bar chart with globe" style="inset:0;background:linear-gradient(180deg,#102436,#1c3a4e 50%,#0a1620)"></div><div class="shade"></div><span class="card-label">OpenPlot</span></div>
<div class="card product-card" style="left:606px;top:2216px;width:259px;height:264px"><div class="media" role="img" aria-label="Night satellite view of a continent" style="inset:0;background:radial-gradient(ellipse at 50% 45%,#4a3a22,#161616 65%)"></div><div class="shade"></div><span class="card-label">MapLedger</span></div>
<div class="card product-card" style="left:878px;top:2216px;width:259px;height:264px"><div class="media" role="img" aria-label="Earth horizon seen from orbit" style="inset:0;background:linear-gradient(180deg,#0c1a33,#2a5a96 40%,#0c1a33 75%)"></div><div class="shade"></div><span class="card-label">Globe Viewer Pro</span></div>

<svg class="abs" style="left:578px;top:2505px" width="44" height="12" aria-hidden="true"><circle cx="6" cy="6" r="3.5" fill="#1a6bb0"/><circle cx="21" cy="6" r="3.5" fill="#c4c8cc"/><circle cx="36" cy="6" r="3.5" fill="#c4c8cc"/></svg>

<section class="cta-band" role="img" aria-label="City skyline at night">
  <h2>Ready To Get Free Consolations<br>For Any Kind Of GIS Work ?</h2>
  <div class="btn btn-square" style="left:729px;top:113px;width:132px;height:36px">Learn more</div>
  <div class="btn btn-square btn-outline" style="left:899px;top:113px;width:132px;height:36px">Get a Quote</div>
</section>

<section class="contact">
  <div class="media" role="img" aria-label="Blue technology backdrop with dotted world map" style="inset:0;background:radial-gradient(ellipse 400px 260px at 300px 300px,rgba(60,130,170,.35),transparent 70%)"></div>
  <h2>Contact us</h2>
  <p class="contact-lead">We are an innovative team of geospatial experts with 25 years of experience in the field of GIS.</p>
  <div class="contact-row" style="top:241px">
    <span class="icon-circle"><svg width="18" height="18" viewBox="0 0 24 24"><path d="M6.6 10.8a15 15 0 0 0 6.6 6.6l2.2-2.2c.3-.3.7-.4 1-.2 1.1.4 2.3.6 3.6.6.6 0 1 .4 1 1V20c0 .6-.4 1-1 1A17 17 0 0 1 3 4c0-.6.4-1 1-1h3.5c.6 0 1 .4 1 1 0 1.3.2 2.5.6 3.6.1.3 0 .7-.2 1z" fill="#1a6bb0"/></svg></span>0198 554 2730
  </div>
  <div class="contact-row" style="top:307px">
    <span class="icon-circle"><svg width="18" height="18" viewBox="0 0 24 24"><path d="M12 2a7 7 0 0 0-7 7c0 5 7 13 7 13s7-8 7-13a7 7 0 0 0-7-7zm0 9.5a2.5 2.5 0 1 1 0-5 2.5 2.5 0 0 1 0 5z" fill="#1a6bb0"/></svg></span>4180 N. Carrow St. #2207<br>Dunmore, CA 92418
  </div>
  <div class="contact-row" style="top:372px">
    <span class="icon-circle"><svg width="20" height="20" viewBox="0 0 24 24" fill="none" stroke="#1a6bb0" stroke-width="1.8"><circle cx="12" cy="12" r="9"/><ellipse cx="12" cy="12" rx="4" ry="9"/><path d="M3 12h18M5 7h14M5 17h14"/></svg></span>www.belvorogroups.com
  </div>
  <div class="form-card">
    <h3>Interested in learning more?</h3>
    <div class="field" style="left:58px;top:90px;width:207px">Your First Name</div>
    <div class="field" style="left:276px;top:90px;width:207px">Your last name</div>
    <div class="field" style="left:58px;top:133px;width:207px">e-mail</div>
    <div class="field" style="left:276px;top:133px;width:207px">Phone. No</div>
    <div class="field msg" style="left:58px;top:179px;width:425px">Message...</div>
    <div class="send">Send</div>
  </div>
</section>

<footer class="footer">
  <div class="brand"><span class="brand-dot"></span>Belvoro Group</div>
  <p class="footer-text">We specialize in providing results-driven GIS solutions for local government and the private sector.</p>
  <div class="footer-col" style="left:609px">
    <h4>Quick <span>Link</span></h4>
    <ul><li>Home</li><li>About us</li><li>Service</li><li>Product</li><li>Contact us</li></ul>
  </div>
  <div class="footer-col" style="left:959px">
    <h4>Service</h4>
    <ul><li>TerraView Online</li><li>TerraView Enterprise</li><li>Dashboards</li><li>Scene Composer</li><li>Custom wid</li></ul>
  </div>
  <div class="footer-rule"></div>
  <div class="footer-bottom" style="left:57px">© Belvoro Groups LLC &nbsp;2024 all rights reserved</div>
  <div class="footer-bottom" style="right:63px">Terms &amp; Conditions</div>
</footer>

</body>
</html>
```